Brom-leigh Sky Harbour Custom Brokers Limited

Shop online from the USA and Ship to Jamaica
Customs Brokerage, Import Export and logistic Services
Address:- 238-240 Halden Brook Road Kingston Jamaica
Email: info@bromleighskyharbour,com
Web: www.bromleighskyharbour.com
Telephone: (876) 555-0148, (876) 555-0193
flyer should be quarter page must print information on back and front

```html
<!DOCTYPE html>
<html lang="en">
<head>
<meta charset="utf-8">
<title>Brom-leigh Sky Harbour – Shop Online Flyer</title>
<link rel="stylesheet" href="https://fonts.googleapis.com/css2?family=Oswald:wght@600;700&family=Open+Sans:wght@400;600;700;800&display=swap">
<style>
  :root{
    --navy:#13294b;
    --navy-deep:#0c1c36;
    --gold:#f4a81d;
    --gold-soft:#ffd36b;
    --paper:#ffffff;
    --ink:#2a2f3a;
    --muted:#5d6472;
    --backdrop:#eceef1;
  }
  *{margin:0;padding:0;box-sizing:border-box}
  html,body{width:1200px;height:2292px;overflow:hidden;background:var(--backdrop)}
  body{font-family:"Open Sans",Arial,sans-serif;color:var(--ink)}
  .flyer{position:absolute;left:100px;top:496px;width:1000px;height:1300px;background:var(--paper);overflow:hidden;box-shadow:0 6px 24px rgba(0,0,0,.12)}
  .flyer-shapes{position:absolute;inset:0;width:1000px;height:1300px}
  .abs{position:absolute}

  .brand{left:40px;top:28px;width:440px}
  .brand-row{display:flex;align-items:center;gap:12px}
  .brand-dot{width:34px;height:34px;border-radius:50%;background:var(--navy);flex:none}
  .brand-name{font-weight:800;font-size:22px;color:var(--navy);line-height:1.1}
  .brand-sub{margin-top:8px;font-size:11.5px;color:var(--muted);line-height:1.5;font-weight:600}

  .headline{left:40px;top:200px;width:520px;color:var(--paper)}
  .headline h1{font-family:"Oswald",Impact,sans-serif;font-weight:700;font-size:78px;line-height:1;letter-spacing:1px}
  .headline p{font-family:"Oswald",Impact,sans-serif;font-weight:600;font-size:32px;line-height:1.15;color:var(--gold);margin-top:10px;text-transform:uppercase}

  .pill{display:inline-block;background:var(--navy);color:var(--paper);font-weight:800;font-size:22px;padding:6px 22px;border-radius:22px;letter-spacing:.5px}
  .pill span{color:var(--gold)}
  .about-head{left:560px;top:612px}
  .about-text{left:560px;top:665px;width:400px;font-size:14.5px;line-height:1.62;color:var(--ink);text-align:justify}
  .services-head{left:40px;top:880px}

  .service{display:flex;flex-direction:column;width:240px}
  .service b{font-size:13.5px;color:var(--navy);text-transform:uppercase;font-weight:800}
  .service small{font-size:12px;color:var(--muted);line-height:1.35}

  .footer{left:0;top:1212px;width:1000px;height:88px;display:flex}
  .footer-phone{width:480px;background:var(--navy);display:flex;align-items:center;gap:16px;padding-left:40px;color:var(--paper);font-weight:800;font-size:30px}
  .footer-web{flex:1;display:flex;align-items:center;gap:12px;padding:0 40px 0 36px;color:var(--navy);font-weight:700;font-size:22px;white-space:nowrap}
  .icon-circle{width:48px;height:48px;border-radius:50%;background:var(--gold);display:flex;align-items:center;justify-content:center;flex:none}
</style>
</head>
<body>
<main class="flyer">
  <svg class="flyer-shapes" viewBox="0 0 1000 1300" aria-hidden="false">
    <defs>
      <linearGradient id="g-woman" x1="0" y1="0" x2="1" y2="1">
        <stop offset="0" stop-color="#e9dccb"/><stop offset=".6" stop-color="#b98c68"/><stop offset="1" stop-color="#6e4a35"/>
      </linearGradient>
      <linearGradient id="g-boxes" x1="0" y1="0" x2="0" y2="1">
        <stop offset="0" stop-color="#f2efea"/><stop offset="1" stop-color="#c69a63"/>
      </linearGradient>
      <linearGradient id="g-hand" x1="0" y1="0" x2="1" y2="1">
        <stop offset="0" stop-color="#c8d3df"/><stop offset="1" stop-color="#a37a5c"/>
      </linearGradient>
      <linearGradient id="g-delivery" x1="0" y1="0" x2="1" y2="1">
        <stop offset="0" stop-color="#dfe7ef"/><stop offset=".55" stop-color="#6f9ac8"/><stop offset="1" stop-color="#c49a6c"/>
      </linearGradient>
      <linearGradient id="g-warehouse" x1="0" y1="0" x2="0" y2="1">
        <stop offset="0" stop-color="#d9e2ea"/><stop offset=".6" stop-color="#8fa3b5"/><stop offset="1" stop-color="#e0b23a"/>
      </linearGradient>
    </defs>

    <g role="img" aria-label="Photo of a smiling woman shopping online at home, with a cargo plane flying overhead">
      <path d="M500 0 H1000 V560 H700 C580 560 500 470 500 360 Z" fill="url(#g-woman)"/>
    </g>
    <path d="M560 440 C590 530 640 575 720 575 H1000" fill="none" stroke="var(--gold)" stroke-width="10"/>

    <path d="M0 160 H560 C620 160 640 230 610 300 L560 420 H0 Z" fill="var(--navy)"/>
    <path d="M0 432 H570" stroke="var(--gold)" stroke-width="8"/>

    <g role="img" aria-label="Photo of stacked cardboard shipping boxes">
      <rect x="40" y="448" width="420" height="130" fill="url(#g-boxes)"/>
    </g>

    <circle cx="560" cy="520" r="108" fill="var(--gold)"/>
    <g role="img" aria-label="Photo of a hand holding a phone for online shopping">
      <circle cx="560" cy="520" r="98" fill="url(#g-hand)"/>
    </g>

    <g role="img" aria-label="Photo of a courier handing a parcel to a customer">
      <rect x="40" y="612" width="440" height="230" rx="6" fill="url(#g-delivery)"/>
    </g>
    <rect x="40" y="842" width="440" height="8" fill="var(--navy)"/>

    <g stroke="var(--navy)" stroke-width="3" fill="none">
      <path d="M140 1055 L240 975"/><path d="M140 1055 L240 1035"/>
      <path d="M140 1055 L240 1095"/><path d="M140 1055 L240 1155"/>
    </g>
    <circle cx="110" cy="1055" r="58" fill="var(--navy)"/>
    <circle cx="110" cy="1055" r="46" fill="none" stroke="var(--gold)" stroke-width="4"/>
    <g fill="var(--paper)">
      <rect x="86" y="1040" width="48" height="34" rx="3"/>
      <rect x="98" y="1030" width="24" height="12" rx="2" fill="none" stroke="var(--paper)" stroke-width="3"/>
    </g>
    <g fill="var(--gold)">
      <circle cx="258" cy="975" r="18"/><circle cx="258" cy="1035" r="18"/>
      <circle cx="258" cy="1095" r="18"/><circle cx="258" cy="1155" r="18"/>
    </g>
    <g stroke="var(--navy)" stroke-width="3" fill="none">
      <path d="M251 975 l5 5 l9 -10"/>
      <path d="M251 1035 l5 5 l9 -10"/>
      <path d="M251 1095 l5 5 l9 -10"/>
      <path d="M251 1155 l5 5 l9 -10"/>
    </g>

    <g role="img" aria-label="Photo of a logistics worker in a hard hat and safety vest at a warehouse">
      <rect x="590" y="935" width="370" height="250" rx="6" fill="url(#g-warehouse)"/>
    </g>
    <path d="M590 1185 H960" stroke="var(--gold)" stroke-width="8"/>
  </svg>

  <header class="abs brand">
    <div class="brand-row">
      <span class="brand-dot"></span>
      <div class="brand-name">Brom-leigh Sky Harbour<br>Custom Brokers Limited</div>
    </div>
    <p class="brand-sub">238-240 Halden Brook Road, Kingston Jamaica<br>info@bromleighskyharbour,com · (876) 555-0148</p>
  </header>

  <section class="abs headline">
    <h1>SHOP ONLINE</h1>
    <p>From the USA and<br>ship to Jamaica</p>
  </section>

  <h2 class="abs about-head pill">ABOUT <span>US</span></h2>
  <p class="abs about-text">Bromleigh Sky Harbour is a trusted customs broker in Kingston. We help families and businesses shop online from the USA and receive their goods in Jamaica quickly and safely. Our team handles customs clearance, duties, import and export paperwork and local delivery, so you can shop with confidence and leave the logistics to us.</p>

  <h2 class="abs services-head pill">OUR <span>SERVICES</span></h2>
  <div class="abs service" style="left:290px;top:958px"><b>Customs Brokerage</b><small>Fast clearance of your goods</small></div>
  <div class="abs service" style="left:290px;top:1018px"><b>Import &amp; Export</b><small>Shipping to and from the USA</small></div>
  <div class="abs service" style="left:290px;top:1078px"><b>Logistic Services</b><small>Safe storage and local delivery</small></div>
  <div class="abs service" style="left:290px;top:1138px"><b>Online Shopping</b><small>Buy in the USA, collect here</small></div>

  <footer class="abs footer">
    <div class="footer-phone">
      <span class="icon-circle">
        <svg width="24" height="24" viewBox="0 0 24 24"><path d="M6.6 10.8a15 15 0 0 0 6.6 6.6l2.2-2.2a1 1 0 0 1 1-.25 11.4 11.4 0 0 0 3.6.57 1 1 0 0 1 1 1V20a1 1 0 0 1-1 1A17 17 0 0 1 3 4a1 1 0 0 1 1-1h3.5a1 1 0 0 1 1 1c0 1.25.2 2.45.57 3.6a1 1 0 0 1-.25 1z" fill="#13294b"/></svg>
      </span>
      (876) 555-0193
    </div>
    <div class="footer-web">
      <span class="icon-circle">
        <svg width="26" height="26" viewBox="0 0 24 24" fill="none" stroke="#13294b" stroke-width="2"><circle cx="12" cy="12" r="9"/><path d="M3 12h18M12 3c3 3.2 3 14.8 0 18M12 3c-3 3.2-3 14.8 0 18"/></svg>
      </span>
      www.bromleighskyharbour.com
    </div>
  </footer>
</main>
</body>
</html>
```